Mine Engineering Consultancy specializing in
* Pit optimization
* Mine Design
* Scheduling
* Mine Rehabilitation

Industry/Entity Type

Mining

Contact Information for Business Card

RVT Mining Pty Ltd
Derek Holloway
Director/Principle Mining Engineer
Mobile 0413582961
Email derek.holloway@rvtmining-example.com

```html
<!DOCTYPE html>
<html lang="en">
<head>
<meta charset="UTF-8">
<title>RVT Mining Pty Ltd – Business Card</title>
<link rel="stylesheet" href="https://fonts.googleapis.com/css2?family=Open+Sans:wght@400;700&family=Tinos&display=swap">
<style>
  :root {
    --backdrop: #c9c9c9;
    --card-black: #000000;
    --strip-dark: #121212;
    --brand-blue: #1e6fc0;
    --stripe-white: #f4f4f4;
    --text-white: #ffffff;
  }
  * { margin: 0; padding: 0; box-sizing: border-box; }
  html, body {
    width: 1200px; height: 900px; overflow: hidden;
    background: var(--backdrop);
  }
  .canvas { position: relative; width: 1200px; height: 900px; }

  .card {
    position: absolute; left: 320px;
    width: 560px; height: 320px;
    background: var(--card-black);
    overflow: hidden;
    box-shadow: 0 6px 18px rgba(0,0,0,0.25);
  }
  .card--back { top: 90px; }
  .card--front { top: 490px; }

  .card__stripe-white {
    position: absolute; left: 0; right: 0;
    height: 7px; background: var(--stripe-white);
  }
  .card__band-blue {
    position: absolute; left: 0; right: 0; bottom: 0;
    height: 32px; background: var(--brand-blue);
  }
  .card--back .card__stripe-white { bottom: 32px; }
  .card--front .card__stripe-white { bottom: 32px; }

  .wordmark {
    font-family: "Tinos", "Times New Roman", serif;
    font-weight: 400;
    color: var(--brand-blue);
    white-space: nowrap;
  }

  /* Back */
  .back__wordmark {
    position: absolute; left: 0; right: 0; top: 95px;
    text-align: center; font-size: 36px;
  }
  .back__services {
    position: absolute; left: 0; right: 0; top: 165px;
    text-align: center;
    font-family: "Open Sans", Arial, sans-serif;
    font-size: 14px; line-height: 20px;
    color: var(--brand-blue);
  }
  .back__services .dot {
    display: inline-block; width: 7px; height: 7px;
    border-radius: 50%; background: var(--brand-blue);
    margin: 0 8px; vertical-align: middle;
  }

  /* Front */
  .front__wordmark {
    position: absolute; left: 30px; top: 52px; font-size: 28px;
  }
  .front__person {
    position: absolute; right: 28px; top: 30px; text-align: right;
    font-family: "Open Sans", Arial, sans-serif;
  }
  .front__name {
    color: var(--brand-blue); font-weight: 700;
    font-size: 17px; letter-spacing: 0.5px; text-transform: uppercase;
  }
  .front__title { color: var(--text-white); font-size: 13px; margin-top: 2px; }

  .front__contact-strip {
    position: absolute; left: 0; right: 0; top: 168px; bottom: 39px;
    background: var(--strip-dark);
  }
  .contact {
    position: absolute;
    font-family: "Open Sans", Arial, sans-serif;
    color: var(--text-white); font-size: 14px;
    display: flex; align-items: center; gap: 7px;
  }
  .contact--phone { left: 30px; top: 24px; }
  .contact--email { right: 28px; bottom: 18px; }
  .contact svg { flex: none; }
</style>
</head>
<body>
<main class="canvas">

  <section class="card card--back" aria-label="Business card back">
    <div class="wordmark back__wordmark">RVT Mining Pty Ltd</div>
    <div class="back__services">
      Pit optimization<span class="dot"></span>Mine Design<span class="dot"></span>Scheduling<br>
      Mine Rehabilitation
    </div>
    <div class="card__stripe-white"></div>
    <div class="card__band-blue"></div>
  </section>

  <section class="card card--front" aria-label="Business card front">
    <div class="front__contact-strip">
      <div class="contact contact--phone">
        <svg width="13" height="11" viewBox="0 0 13 11" aria-hidden="true">
          <path d="M1 3 Q6.5 -1 12 3 L10.5 5 L8.5 4 L8.5 3 Q6.5 2 4.5 3 L4.5 4 L2.5 5 Z" fill="var(--brand-blue)"/>
          <rect x="3" y="5.5" width="7" height="5" rx="1" fill="var(--brand-blue)"/>
        </svg>
        <span>0413582961</span>
      </div>
      <div class="contact contact--email">
        <span>derek.holloway@rvtmining-example.com</span>
        <svg width="13" height="10" viewBox="0 0 13 10" aria-hidden="true">
          <rect x="0.5" y="0.5" width="12" height="9" fill="var(--brand-blue)"/>
          <path d="M0.5 0.5 L6.5 5.5 L12.5 0.5" fill="none" stroke="var(--strip-dark)" stroke-width="1"/>
        </svg>
      </div>
    </div>

    <div class="wordmark front__wordmark">RVT Mining Pty Ltd</div>
    <div class="front__person">
      <div class="front__name">Derek Holloway</div>
      <div class="front__title">Director/Principle Mining Engineer</div>
    </div>

    <div class="card__stripe-white"></div>
    <div class="card__band-blue"></div>
  </section>

</main>
</body>
</html>
```